Flyer Design Project - law firm

I need a design for an advertising flyer for my law firm.
Ideally the size of the document will be one page A4.
I have attached a copy of the logo. I would like the lettering for 'Marwood Legal' to be all the same size, rather than the 'S' and 'L' being slightly larger
The flyer must include the text below:
Wills
Anyone who owns property or investments or has family obligations should have a Will to ensure that their assets are distributed in accordance with their wishes and that their children are cared for by the guardians of their choosing. Without a Will, these vital decisions are determined by the government or the courts of the State or Territory which you lived in at the time of your death.
Marwood Legal can assist you in the preparation of a legal will tailored to your particular circumstances to ensure that your wishes are followed.
We are offering Tollbeck- Crane Harbour clients a free discussion of their will requirements and a heavily discounted standard wills package of
$330.00* for a single will
$550.00* for couples wills
These prices are only valid prior to your conveyancing settlement for standard wills (e.g. not including a testamentary trust or other complications.
Please contact us on or provide Tollbeck Crane Harbour with authority for us to contact you today.
Updates
Hi All,
I have posted a copy of the proposed logo. Please note that I need the wording of 'Marwood Legal' to all be the same size, rather than the 'S' and 'L' being slightly larger.
If you require anything further please let me know.
Thanks
I have added copies of the logo in ups format,
If you require anything further please let know.
Thanks for your assistance.

```html
<!DOCTYPE html>
<html lang="en">
<head>
<meta charset="utf-8">
<title>Marwood Legal – Wills Flyer</title>
<link href="https://fonts.googleapis.com/css2?family=Source+Sans+3:wght@400;600;700&display=swap" rel="stylesheet">
<style>
  :root{
    --orange:#f26a2e;
    --orange-soft:#f7a072;
    --ink:#1d1d1d;
    --paper:#ececec;
    --paper-light:#f2f2f2;
    --stage:#d9d9d9;
    --divider:#f39a66;
  }
  *{box-sizing:border-box;margin:0;padding:0}
  html,body{width:1045px;height:1200px;overflow:hidden}
  body{background:var(--stage);font-family:"Source Sans 3",Arial,sans-serif;color:var(--ink);position:relative}
  .flyer{position:absolute;left:122px;top:35px;width:800px;height:1130px;background:var(--paper);box-shadow:0 4px 14px rgba(0,0,0,.25);overflow:hidden}

  .masthead{position:absolute;left:0;top:0;width:100%;height:144px;background:var(--paper-light);border-bottom:5px solid var(--orange)}
  .brand{position:absolute;left:36px;top:47px;display:flex;align-items:center;gap:14px}
  .brand-mark{width:48px;height:48px;border-radius:50%;background:var(--orange)}
  .brand-name{font-size:36px;font-weight:400;text-transform:uppercase;letter-spacing:1px;color:var(--ink)}
  .call-cta{position:absolute;right:22px;top:30px;text-align:right}
  .call-cta .label{color:var(--orange);font-size:37px;line-height:1.1}
  .call-cta .number{font-size:28px;margin-top:6px}

  .team-photo{position:absolute;left:0;top:152px;width:100%;height:428px;
    background:linear-gradient(100deg,#5a2a1c 0%,#a79e74 18%,#c6bf91 45%,#6d6e74 70%,#dfe3e6 100%)}

  .content{position:absolute;left:30px;top:602px;width:740px}
  .section-title{display:flex;align-items:center;gap:8px;color:var(--orange);font-size:23px;font-weight:700}
  .section-title::before{content:"";width:10px;height:10px;border:1.5px solid var(--ink);border-radius:50%}
  .content p{font-size:15.5px;line-height:22px;margin-top:8px}
  .content p.lead{margin-top:6px}
  .content p.assist{margin-top:18px}

  .offer{position:absolute;left:30px;top:836px;width:507px;height:148px;background:var(--orange);border-radius:8px;
    box-shadow:0 3px 8px rgba(0,0,0,.3);color:#fff;padding:14px 14px}
  .offer .intro{font-size:15px;line-height:22px}
  .offer .prices{display:flex;gap:22px;font-size:16.5px;font-weight:700;margin-top:20px}
  .offer .note{font-size:11.5px;margin-top:18px}

  .faint-ring{position:absolute;left:610px;top:838px;width:140px;height:140px;border-radius:50%;border:9px solid var(--orange);opacity:.12}

  .closing{position:absolute;left:30px;top:1006px;font-size:15.5px}

  .contact-bar{position:absolute;left:0;top:1045px;width:100%;height:85px;border-top:3px solid var(--orange);background:var(--paper-light)}
  .contact-row{display:flex;align-items:center;height:64px;padding:0 26px}
  .contact-cell{font-size:14px;line-height:20px;padding:0 30px;border-right:2px solid var(--divider)}
  .contact-cell:first-child{padding-left:0}
  .contact-cell:last-child{border-right:none;margin-left:auto;padding-right:0;text-align:right}
  .contact-cell .label{color:var(--orange);font-size:17px}
  .contact-cell .number{font-size:17px}
  .icon-line{display:flex;align-items:center;gap:6px}
  .icon-line svg{width:11px;height:11px;flex:none}
  .dot{width:10px;height:10px;border-radius:50%;background:#3b5b9a;flex:none}
  .base-band{position:absolute;left:0;bottom:0;width:100%;height:18px;background:linear-gradient(90deg,var(--orange),var(--orange-soft))}
</style>
</head>
<body>
<main class="flyer">
  <header class="masthead">
    <div class="brand">
      <span class="brand-mark"></span>
      <span class="brand-name">Marwood Legal</span>
    </div>
    <div class="call-cta">
      <div class="label">Call Us Today</div>
      <div class="number">97-5128-3360</div>
    </div>
  </header>

  <div class="team-photo" role="img" aria-label="Photo of four lawyers working around a conference table in an office"></div>

  <section class="content">
    <h2 class="section-title">Wills</h2>
    <p class="lead">Anyone who owns property or investments or has family obligations should have a will to ensure that their assets are distributed in accordance with their wishes and that their children are cared for by the guardians of their choosing.</p>
    <p>Without a will, these vital decisions are determined by the government or the courts of the state or territory which you lived in at the time of your death.</p>
    <p class="assist">Marwood Legal Can Assist You In The Preparation Of A Legal Will Tailored To Your Particular Circumstances To Ensure That Your Wishes Are Followed.</p>
  </section>

  <aside class="offer">
    <p class="intro">We Are Offering Tollbeck- Crane Harbour Clients A Free Discusion Of Their Will Requirements And A Heavily Discounted Standard Wills Package of</p>
    <div class="prices"><span>&gt; $330.00* for a single will</span><span>&gt; $550.00* for couples wills</span></div>
    <p class="note">These Prices Are Only Valid Prior To Your Conveyancing Settlement For Standard Wills</p>
  </aside>
  <div class="faint-ring"></div>

  <p class="closing">Please Contact Us On Or Provide Tollbeck Crane Harbour With Authority For Us To Contact You Today.</p>

  <footer class="contact-bar">
    <div class="contact-row">
      <div class="contact-cell">
        <div class="label">Call Us Today</div>
        <div class="number">97-5128-3360</div>
      </div>
      <div class="contact-cell">
        <div>Street Name, City Name</div>
        <div>State, City Zip Code</div>
      </div>
      <div class="contact-cell">
        <div class="icon-line"><svg viewBox="0 0 12 12"><path d="M6 1 L11 6 H9.5 V11 H2.5 V6 H1 Z" fill="#f26a2e"/></svg>14-2781-9053</div>
        <div class="icon-line"><span class="dot"></span>marwoodlegal</div>
      </div>
      <div class="contact-cell">
        <div class="icon-line" style="justify-content:flex-end"><svg viewBox="0 0 12 12"><rect x="1" y="2.5" width="10" height="7" rx="1" fill="#f26a2e"/><path d="M1.5 3 L6 6.5 L10.5 3" stroke="#fff" fill="none"/></svg>infomarwoodlegal.com</div>
        <div class="icon-line" style="justify-content:flex-end"><svg viewBox="0 0 12 12"><circle cx="6" cy="6" r="5" fill="#f26a2e"/><path d="M1 6 H11 M6 1 C3.5 4 3.5 8 6 11 M6 1 C8.5 4 8.5 8 6 11" stroke="#fff" stroke-width=".8" fill="none"/></svg>www.marwoodlegal.com</div>
      </div>
    </div>
    <div class="base-band"></div>
  </footer>
</main>
</body>
</html>
```